i am creating an a new cold brew coffee and need a standard format for 5 different flavours. the PDF with 5 colours is what i created as a format and the one page PDF is the style i like but am happy yo move away from it.. the images are the style i like

i am looking for a nice clean tidy but standard out label that will pop off a brown paper backing.

Target Market(s)

18-40 Yr old coffee lovers wanting a high end cold brew coffee

Font styles to use
Serif
Sans Serif

Colors

Designer to choose colors to be used in the design.

Requirements
Must have
• i want a standard format that a component can change colour with flavours, brown paper background. i need the nutritional content box at the back ( as per PDF ) and i would like the text added also, as this is a description of the product
Nice to have
• i like the tidy clinical look of the font pharma bold condensed
• the PDF's show the flavours.. the one with a brown background is something i have seen that i like and the images are the styles i like .

```html
<!DOCTYPE html>
<html lang="en">
<head>
<meta charset="utf-8">
<title>Tandem Brews – Cold Brew Label System</title>
<link rel="stylesheet" href="https://fonts.googleapis.com/css2?family=Anton&family=Sorts+Mill+Goudy&display=swap">
<style>
:root{
  --kraft:#d8b98a;
  --ink:#231f20;
  --paper:#ffffff;
  --ginger:#ffd200;
  --blackberry:#a58dc3;
  --chocolate:#b8875a;
  --coconut:#f7941d;
  --citrus:#a9c23a;
  --rule:#555;
}
*{box-sizing:border-box;margin:0;padding:0}
html,body{width:1200px;height:960px;overflow:hidden}
body{background:var(--kraft);position:relative;color:var(--ink);font-family:"Sorts Mill Goudy",Georgia,serif}
.display{font-family:"Anton","Arial Narrow",sans-serif;text-transform:uppercase;letter-spacing:-0.5px}

/* Flavour range */
.mini{position:absolute;top:165px;width:178px;height:192px;background:var(--paper);text-align:center}
.mini .badge{position:absolute;left:44px;top:0;width:34px;height:33px;background:var(--accent);font-size:12px;line-height:33px}
.mini .type{position:absolute;top:43px;width:100%;font-size:12px}
.mini .band{position:absolute;top:68px;width:100%;height:50px;background:var(--accent);font-size:27px;line-height:50px}
.mini .flavour{position:absolute;top:126px;width:100%;font-size:12px}
.mini .size{position:absolute;top:158px;width:100%;font-size:6px}
.mini .origin{position:absolute;top:171px;width:100%;font-size:5.5px}
.ginger{--accent:var(--ginger)}
.blackberry{--accent:var(--blackberry)}
.chocolate{--accent:var(--chocolate)}
.coconut{--accent:var(--coconut)}
.citrus{--accent:var(--citrus)}

/* Full wrap label */
.wrap{position:absolute;left:144px;top:480px;width:881px;height:406px;background:var(--paper);--accent:var(--ginger)}
.divider{position:absolute;top:0;height:100%;border-left:1px dashed var(--rule)}
.panel{position:absolute;top:0;height:100%}
.nutrition{left:26px;width:220px;font-size:11.5px}
.nutrition h2{position:absolute;top:24px;font-size:13px;font-weight:400}
.nutrition .serve{position:absolute;top:46px;width:200px;line-height:15px}
.nutrition .serve span{position:absolute;top:0}
.nutrition .rows{position:absolute;top:85px;list-style:none;line-height:18px}
.nutrition .ingredients{position:absolute;top:226px;line-height:15px}
.nutrition .care{position:absolute;top:290px;list-style:none;line-height:15px;width:200px}
.nutrition .care li{padding-left:10px;position:relative}
.nutrition .care li::before{content:"";position:absolute;left:0;top:5px;width:4px;height:4px;background:var(--ink)}
.tag{position:absolute;top:352px;display:flex;align-items:center;gap:7px;font-size:9.5px;line-height:10px;text-transform:uppercase}
.tag b{display:block;width:23px;height:23px;background:var(--accent);font-weight:400;font-size:13px;line-height:23px;text-align:center}
.front{left:250px;width:376px;text-align:center}
.front .badge{position:absolute;left:93px;top:0;width:72px;height:68px;background:var(--accent);font-size:29px;line-height:68px}
.front .type{position:absolute;top:107px;width:100%;font-size:26px}
.front .band{position:absolute;top:143px;width:100%;height:107px;background:var(--accent);font-size:58px;line-height:107px}
.front .flavour{position:absolute;top:268px;width:100%;font-size:26px}
.front .size{position:absolute;top:333px;width:100%;font-size:13px}
.front .origin{position:absolute;top:362px;width:100%;font-size:13px}
.story{left:654px;width:222px;font-size:10.6px;line-height:14.4px}
.story p{position:absolute;left:0;white-space:nowrap}
.story h3{position:absolute;top:289px;font-size:12.5px;font-weight:400}
.refund{top:352px}
.refund b{font-size:11px}
</style>
</head>
<body>

<section class="range">
  <article class="mini ginger" style="left:89px">
    <div class="badge display">New</div><div class="type">Cold Brew Coffee</div>
    <div class="band display">Tandem Brews</div><div class="flavour">Sparkling Ginger</div>
    <div class="size display">330ml</div><div class="origin">100% Australian Made + Owned</div>
  </article>
  <article class="mini blackberry" style="left:300px">
    <div class="badge display">New</div><div class="type">Cold Brew Coffee</div>
    <div class="band display">Tandem Brews</div><div class="flavour">Sparkling Blackberry</div>
    <div class="size display">330ml</div><div class="origin">100% Australian Made + Owned</div>
  </article>
  <article class="mini chocolate" style="left:510px;top:163px">
    <div class="badge display">New</div><div class="type">Cold Brew Coffee</div>
    <div class="band display">Tandem Brews</div><div class="flavour">Sparkling Chocolate</div>
    <div class="size display">330ml</div><div class="origin">100% Australian Made + Owned</div>
  </article>
  <article class="mini coconut" style="left:721px;top:163px;width:181px;height:195px">
    <div class="badge display">New</div><div class="type">Cold Brew Coffee</div>
    <div class="band display">Tandem Brews</div><div class="flavour">Coconut Nectar</div>
    <div class="size display">330ml</div><div class="origin">100% Australian Made + Owned</div>
  </article>
  <article class="mini citrus" style="left:935px">
    <div class="badge display">New</div><div class="type">Cold Brew Coffee</div>
    <div class="band display">Tandem Brews</div><div class="flavour">Sparkling Citrus</div>
    <div class="size display">330ml</div><div class="origin">100% Australian Made + Owned</div>
  </article>
</section>

<section class="wrap">
  <div class="panel nutrition">
    <h2 class="display">Nutritional Information</h2>
    <div class="serve">Servings: 1<br>Serving : 330ml
      <span style="left:100px">Av per<br>Serv.</span>
      <span style="left:150px">Av per<br>100g</span>
    </div>
    <ul class="rows"><li>Energy</li><li>Protein</li><li>Fat, Total</li><li>- Saturated</li><li>Carbs</li><li>- Sugars</li><li>Sodium</li></ul>
    <p class="ingredients">All Organic Ingredients:<br>Cold Brew Coffee, Arabica Beans,<br>Raw Coconut Nectar, Ginger 4%</p>
    <ul class="care"><li>Keep Refrigerated after opening and consume within 2 days from opening</li><li>Please do not shake</li></ul>
    <div class="tag" style="left:0"><b class="display">NV</b><span>Naturally<br>Vegan</span></div>
    <div class="tag" style="left:114px"><b class="display">GF</b><span>Gluten<br>Free</span></div>
  </div>
  <div class="divider" style="left:250px"></div>

  <div class="panel front">
    <div class="badge display">New</div>
    <div class="type">Cold Brew Coffee</div>
    <div class="band display">Tandem Brews</div>
    <div class="flavour">Sparkling Ginger</div>
    <div class="size display">330ml</div>
    <div class="origin">100% Australian Made + Owned</div>
  </div>
  <div class="divider" style="left:626px"></div>

  <div class="panel story">
    <p style="top:33px">Tandem Brews made this Cold brew coffee<br>to make you think clearer, feel motivated<br>and to just be a better person. We wont<br>claim any responsibility for the achievements<br>you make while drinking our brews, that<br>brilliance was always about you, we just helped<br>you bring it out.</p>
    <p style="top:142px">We know that if you have finished the bottle<br>you will be feeling too good to be reading this<br>label in its entirety. So we will finish it here<br>so you can continue on your motivated way.</p>
    <p style="top:209px">Want to contact us? Sure do it here:<br>www.tandembrews.example</p>
    <p style="top:248px">Or here 42 Kestrel Lane, Fernvale<br>NSW 2999 or on this 0400 000 123</p>
    <h3 class="display">World First Release:</h3>
    <p style="top:306px">Call 0400 111 222<br>For distribution enquiries.</p>
    <div class="tag refund" style="left:0"><b class="display">10¢</b><span>Refund at collection depots<br>########</span></div>
  </div>
</section>

</body>
</html>
```